Copper Lantern Gatherings need a stand out marketing flyer.

Copper Lantern Gatherings is a company that runs empowerment retreats and bespoke corporate training in creating positive change.
We would like an A5 flyer that is 2 sided. the reverse side of the flyer we would like some of our testimonial quotes.

The flyer should be punchy and not too heavy with wordy detail but have enough detail so people can see what we offer. Encouraging people to contact us to find out more

Our empowerment retreats help people to live without limits, be fierce and wild, be creative and courageous, be fearless and free.
Leave behind
- lack of self esteem
- lack of personal power
- lack of focus
- old fears and beliefs
- overwhelm
Find new
- confidence
- personal empowerment
- commitment
- courage
- resilience

Contact details:
website: www.copperlanternevents.example.co.uk
email: info@copperlanterngatherings.example.com
Harriet Colbane Tel: 07700 900 318
Joanna Pirrett Tel: 07700 900 572

You can use as much of the detail above in your design as you would like..
I attach our logos. you can pick which ever design you prefer to work with. I have also attached a file that contains the testimonials for the reverse of the slide. I've also attached a few pictures but these aren't necessary in your design they are just an option/idea for you to consider. You can use alternative pictures should you wish to.

Details for our up and coming events can be found on our website

```html
<!DOCTYPE html>
<html lang="en">
<head>
<meta charset="utf-8">
<title>Copper Lantern Gatherings – A5 Flyer</title>
<link rel="stylesheet" href="https://fonts.googleapis.com/css2?family=Open+Sans:wght@400;600&display=swap">
<style>
  :root {
    --canvas: #e4e4e4;
    --paper: #ffffff;
    --ink: #2b2b2d;
    --ink-soft: #4a4a4c;
    --charcoal: #3a3a3d;
    --blue: #1e9fd8;
    --blue-deep: #0d4f9e;
    --navy: #1b2a6b;
    --sky: #4db5e8;
    --quote-bg: #ebecec;
    --photo-warm-a: #c9d3d4;
    --photo-warm-b: #d9b98e;
    --photo-grey-a: #9c9c9c;
    --photo-grey-b: #6f6f6f;
  }
  * { box-sizing: border-box; margin: 0; padding: 0; }
  html, body { width: 1200px; height: 827px; overflow: hidden; }
  body {
    background: var(--canvas);
    font-family: "Open Sans", Arial, sans-serif;
    color: var(--ink);
    position: relative;
  }
  .flyer {
    position: absolute;
    top: 83px;
    width: 464px;
    height: 656px;
    background: var(--paper);
    overflow: hidden;
  }
  .flyer--front { left: 111px; }
  .flyer--back { left: 630px; }
  .flyer__shapes { position: absolute; inset: 0; width: 100%; height: 100%; }

  .brand {
    position: absolute;
    top: 12px;
    width: 74px;
    text-align: center;
    color: var(--blue-deep);
    font-size: 10px;
    font-weight: 600;
    line-height: 1.15;
    letter-spacing: 0.02em;
  }
  .brand__dot {
    display: block;
    width: 18px; height: 18px;
    margin: 0 auto 5px;
    border-radius: 50%;
    background: var(--blue);
  }
  .flyer--front .brand { left: 61px; }
  .flyer--back .brand { left: 353px; }

  .headline {
    position: absolute;
    left: 0; right: 0;
    text-align: center;
    font-weight: 600;
    text-transform: uppercase;
    color: var(--ink);
  }
  .front-title { top: 263px; font-size: 13.6px; letter-spacing: 0.01em; }
  .intro {
    position: absolute;
    top: 296px; left: 32px; right: 22px;
    text-align: center;
    font-size: 11.3px;
    line-height: 1.45;
    color: var(--ink-soft);
  }

  .change-list {
    position: absolute;
    top: 357px;
    width: 190px;
    list-style: none;
    color: #ffffff;
    font-size: 11.3px;
  }
  .change-list--behind { left: 30px; }
  .change-list--new { left: 272px; }
  .change-list__title {
    color: var(--sky);
    font-size: 11.3px;
    margin-bottom: 6px;
    text-transform: uppercase;
    letter-spacing: 0.02em;
  }
  .change-list li {
    display: flex;
    align-items: center;
    height: 18.8px;
  }
  .change-list li svg { width: 9px; height: 9px; margin-right: 7px; flex: none; }

  .contact-title { top: 609px; }
  .contact {
    position: absolute;
    top: 527px; left: 0; right: 0;
    text-align: center;
  }
  .contact__title {
    font-size: 15.4px;
    font-weight: 600;
    text-transform: uppercase;
    margin-bottom: 7px;
  }
  .contact__line {
    font-size: 9.9px;
    line-height: 17.6px;
    color: var(--ink-soft);
  }

  .footer-url {
    position: absolute;
    left: 60px; right: 0;
    top: 626px;
    text-align: center;
    color: #ffffff;
    font-size: 12.6px;
  }

  .back-title { top: 262px; font-size: 13.6px; }
  .back-subtitle {
    position: absolute;
    top: 282px; left: 0; right: 0;
    text-align: center;
    font-size: 12px;
    color: var(--ink-soft);
  }
  .quotes {
    position: absolute;
    top: 325px; left: 16px;
    width: 433px;
    display: grid;
    grid-template-columns: repeat(3, 139px);
    grid-template-rows: repeat(2, 118px);
    gap: 8px 8px;
  }
  .quote {
    background: var(--quote-bg);
    display: flex;
    align-items: center;
    justify-content: center;
    text-align: center;
    padding: 6px 14px;
    font-size: 9.7px;
    line-height: 1.5;
    color: var(--ink);
  }
</style>
</head>
<body>

<section class="flyer flyer--front">
  <svg class="flyer__shapes" viewBox="0 0 420 595" preserveAspectRatio="none" aria-hidden="true">
    <defs>
      <linearGradient id="warmPhoto" x1="0" y1="0" x2="0" y2="1">
        <stop offset="0" stop-color="var(--photo-warm-a)"/>
        <stop offset="0.55" stop-color="#d8cbb4"/>
        <stop offset="1" stop-color="var(--photo-warm-b)"/>
      </linearGradient>
      <linearGradient id="blueFade" x1="0" y1="0" x2="1" y2="1">
        <stop offset="0" stop-color="var(--blue)"/>
        <stop offset="1" stop-color="var(--blue-deep)"/>
      </linearGradient>
      <linearGradient id="footerBand" x1="0" y1="0" x2="1" y2="0">
        <stop offset="0" stop-color="var(--blue)"/>
        <stop offset="1" stop-color="var(--navy)"/>
      </linearGradient>
    </defs>
    <polygon points="140,0 420,0 420,205 50,205 50,85" fill="url(#warmPhoto)"
             role="img" aria-label="Photo: a hand holding a large key towards a seated wooden figure with a keyhole in its chest"/>
    <polygon points="0,35 50,85 0,135" fill="url(#blueFade)"/>
    <polygon points="0,120 0,205 130,205" fill="var(--charcoal)"/>
    <polygon points="130,205 340,160 420,205" fill="#ffffff"/>
    <polygon points="420,128 340,160 420,200" fill="url(#blueFade)"/>
    <rect x="0" y="315" width="420" height="133" fill="var(--charcoal)"/>
    <polygon points="201,448 225,448 213,456" fill="var(--charcoal)"/>
    <polygon points="55,557 420,557 420,595 20,595" fill="url(#footerBand)"/>
    <polygon points="0,595 30,540 75,595" fill="var(--charcoal)"/>
  </svg>

  <div class="brand"><span class="brand__dot"></span>Copper Lantern Gatherings</div>

  <h1 class="headline front-title">Empowerment retreats and bespoke corporate training</h1>
  <p class="intro">Our empowerment retreats help people to live without limits, be fierce and wild, be creative and courageous, be fearless and free.</p>

  <ul class="change-list change-list--behind">
    <li class="change-list__title">Leave behind</li>
    <li><svg viewBox="0 0 10 10"><circle cx="5" cy="5" r="4.2" fill="none" stroke="var(--sky)" stroke-width="1.2"/><path d="M4 3 L6 5 L4 7" fill="none" stroke="var(--sky)" stroke-width="1.2"/></svg>lack of self esteem</li>
    <li><svg viewBox="0 0 10 10"><circle cx="5" cy="5" r="4.2" fill="none" stroke="var(--sky)" stroke-width="1.2"/><path d="M4 3 L6 5 L4 7" fill="none" stroke="var(--sky)" stroke-width="1.2"/></svg>lack of personal power</li>
    <li><svg viewBox="0 0 10 10"><circle cx="5" cy="5" r="4.2" fill="none" stroke="var(--sky)" stroke-width="1.2"/><path d="M4 3 L6 5 L4 7" fill="none" stroke="var(--sky)" stroke-width="1.2"/></svg>lack of focus</li>
    <li><svg viewBox="0 0 10 10"><circle cx="5" cy="5" r="4.2" fill="none" stroke="var(--sky)" stroke-width="1.2"/><path d="M4 3 L6 5 L4 7" fill="none" stroke="var(--sky)" stroke-width="1.2"/></svg>old fears and beliefs</li>
    <li><svg viewBox="0 0 10 10"><circle cx="5" cy="5" r="4.2" fill="none" stroke="var(--sky)" stroke-width="1.2"/><path d="M4 3 L6 5 L4 7" fill="none" stroke="var(--sky)" stroke-width="1.2"/></svg>overwhelm</li>
  </ul>

  <ul class="change-list change-list--new">
    <li class="change-list__title">Find new</li>
    <li><svg viewBox="0 0 10 10"><circle cx="5" cy="5" r="4.2" fill="none" stroke="var(--sky)" stroke-width="1.2"/><path d="M4 3 L6 5 L4 7" fill="none" stroke="var(--sky)" stroke-width="1.2"/></svg>confidence</li>
    <li><svg viewBox="0 0 10 10"><circle cx="5" cy="5" r="4.2" fill="none" stroke="var(--sky)" stroke-width="1.2"/><path d="M4 3 L6 5 L4 7" fill="none" stroke="var(--sky)" stroke-width="1.2"/></svg>personal empowerment</li>
    <li><svg viewBox="0 0 10 10"><circle cx="5" cy="5" r="4.2" fill="none" stroke="var(--sky)" stroke-width="1.2"/><path d="M4 3 L6 5 L4 7" fill="none" stroke="var(--sky)" stroke-width="1.2"/></svg>commitment</li>
    <li><svg viewBox="0 0 10 10"><circle cx="5" cy="5" r="4.2" fill="none" stroke="var(--sky)" stroke-width="1.2"/><path d="M4 3 L6 5 L4 7" fill="none" stroke="var(--sky)" stroke-width="1.2"/></svg>courage</li>
    <li><svg viewBox="0 0 10 10"><circle cx="5" cy="5" r="4.2" fill="none" stroke="var(--sky)" stroke-width="1.2"/><path d="M4 3 L6 5 L4 7" fill="none" stroke="var(--sky)" stroke-width="1.2"/></svg>resilience</li>
  </ul>

  <div class="contact">
    <h2 class="contact__title">Contact us to find out more</h2>
    <p class="contact__line">Harriet Colbane p: 07700 900 318</p>
    <p class="contact__line">Joanna Pirrett p: 07700 900 572</p>
    <p class="contact__line">info@copperlanterngatherings.example.com</p>
  </div>

  <p class="footer-url">www.copperlanternevents.example.co.uk</p>
</section>

<section class="flyer flyer--back">
  <svg class="flyer__shapes" viewBox="0 0 420 595" preserveAspectRatio="none" aria-hidden="true">
    <defs>
      <linearGradient id="greyPhoto" x1="0" y1="0" x2="0" y2="1">
        <stop offset="0" stop-color="var(--photo-grey-b)"/>
        <stop offset="0.6" stop-color="var(--photo-grey-a)"/>
        <stop offset="1" stop-color="#b5b5b5"/>
      </linearGradient>
      <linearGradient id="blueFadeBack" x1="0" y1="0" x2="1" y2="1">
        <stop offset="0" stop-color="var(--blue)"/>
        <stop offset="1" stop-color="var(--blue-deep)"/>
      </linearGradient>
      <linearGradient id="footerBandBack" x1="0" y1="0" x2="1" y2="0">
        <stop offset="0" stop-color="var(--blue)"/>
        <stop offset="1" stop-color="var(--navy)"/>
      </linearGradient>
    </defs>
    <polygon points="0,0 252,0 360,110 330,205 0,205" fill="url(#greyPhoto)"
             role="img" aria-label="Photo: a hand labelled fear holding the strings of a wooden figure that is pulling away"/>
    <polygon points="420,35 355,105 420,175" fill="url(#blueFadeBack)"/>
    <polygon points="330,205 420,128 420,205" fill="var(--charcoal)"/>
    <polygon points="55,557 420,557 420,595 20,595" fill="url(#footerBandBack)"/>
    <polygon points="0,595 30,540 75,595" fill="var(--charcoal)"/>
  </svg>

  <div class="brand"><span class="brand__dot"></span>Copper Lantern Gatherings</div>

  <h1 class="headline back-title">Testimonial quotes</h1>
  <p class="back-subtitle">Copper Lantern Gatherings</p>

  <div class="quotes">
    <blockquote class="quote">Do not hesitate, just book it! It will transform and enhance your life.</blockquote>
    <blockquote class="quote">If you have a chance to do it then do it, it's one of the best experience of my life.</blockquote>
    <blockquote class="quote">The most wonderful weekend of self-discovery and would recommend it to everyone.</blockquote>
    <blockquote class="quote">I've met the most amazing people and feel like I am well equipped with the tools now to help myself physically and mentally. The best self-care I've ever invested in.</blockquote>
    <blockquote class="quote">It's changed my life, given me perspective and time to develop myself. I've met the most amazing people and learnt so much. It's worth every penny.</blockquote>
    <blockquote class="quote">I can't thank Copper Lantern enough for the tools they have metaphorically equipped me with. They are amazing at what they do.</blockquote>
  </div>

  <p class="footer-url">www.copperlanternevents.example.co.uk</p>
</section>

</body>
</html>
```